Upscale business cards needed for family office

We would like professional business cards created for employees of our family office. Relatively simple and straightforward, but also with a unique element to set them apart. Probably stick with neutral and simple colors that mesh well with the colors in the logo. We need space for the traditional elements, including name, title, address, email/phone number.

Industry/Entity Type

Business

Contact Information for Business Card

Space for name, title, phone number, email, address

```html
<!DOCTYPE html>
<html lang="en">
<head>
<meta charset="utf-8">
<title>Halden &amp; Rowe — Business Cards</title>
<link rel="stylesheet" href="https://fonts.googleapis.com/css2?family=Arimo:wght@400;700&display=swap">
<style>
  :root {
    --backdrop: #3b322d;
    --card: #141414;
    --card-edge: #0a0a0a;
    --mark-panel: #ffffff;
    --mark-frame: #b9bcbf;
    --mark-ink: #4a5560;
    --accent: #1a9fd6;
    --text-light: #f2f2f2;
    --divider: #6d6d6d;
  }
  * { box-sizing: border-box; margin: 0; padding: 0; }
  html, body {
    width: 1200px; height: 780px; overflow: hidden;
    background: var(--backdrop);
    font-family: "Arimo", Arial, sans-serif;
  }
  .canvas { position: relative; width: 1200px; height: 780px; }
  .card {
    position: absolute; width: 520px; height: 300px;
    background: var(--card);
    border-radius: 4px;
    box-shadow: 0 14px 30px rgba(0,0,0,.45), 0 0 0 1px var(--card-edge);
  }
  .card--front { left: 70px; top: 90px; }
  .card--back  { left: 610px; top: 390px; }

  .brand-block {
    position: absolute;
    width: 168px; height: 168px;
    background: var(--mark-panel);
    border: 5px solid var(--mark-frame);
    display: flex; align-items: center; justify-content: center;
    text-align: center;
  }
  .card--front .brand-block { left: 176px; top: 66px; }
  .card--back .brand-block { left: 40px; top: 66px; }
  .brand-name {
    font-family: "Arimo", Arial, sans-serif;
    font-weight: 400; font-size: 27px; line-height: 1.15;
    color: var(--mark-ink);
  }

  .divider {
    position: absolute; left: 262px; top: 44px;
    width: 1px; height: 212px; background: var(--divider);
  }
  .details { position: absolute; left: 290px; top: 78px; }
  .person-name { color: var(--text-light); font-size: 25px; line-height: 1; }
  .person-title { color: var(--accent); font-size: 19px; margin-top: 3px; }
  .contact-list { list-style: none; margin-top: 26px; }
  .contact-item {
    display: flex; align-items: center; gap: 12px;
    color: var(--text-light); font-size: 17px; height: 28px;
  }
  .contact-icon {
    width: 16px; height: 16px; flex: none;
    background: var(--accent); border-radius: 2px;
    display: flex; align-items: center; justify-content: center;
  }
</style>
</head>
<body>
<main class="canvas">
  <section class="card card--front" aria-label="Card front">
    <div class="brand-block"><span class="brand-name">Halden<br>&amp; Rowe</span></div>
  </section>

  <section class="card card--back" aria-label="Card back">
    <div class="brand-block"><span class="brand-name">Halden<br>&amp; Rowe</span></div>
    <div class="divider"></div>
    <div class="details">
      <p class="person-name">Owen Pascal</p>
      <p class="person-title">Managing Director</p>
      <ul class="contact-list">
        <li class="contact-item">
          <span class="contact-icon"><svg width="10" height="10" viewBox="0 0 10 10"><path d="M2 1 L4 1 L4.6 3 L3.5 3.8 Q4.5 5.8 6.2 6.5 L7 5.4 L9 6 L9 8 Q5.5 8.8 3 6.5 Q1 4.5 2 1Z" fill="#111"/></svg></span>
          021-555-0142
        </li>
        <li class="contact-item">
          <span class="contact-icon"><svg width="10" height="8" viewBox="0 0 10 8"><rect x=".5" y=".5" width="9" height="7" fill="none" stroke="#111"/><path d="M.5 .5 L5 4.5 L9.5 .5" fill="none" stroke="#111"/></svg></span>
          owen@haldenrowe.com
        </li>
        <li class="contact-item">
          <span class="contact-icon"><svg width="8" height="11" viewBox="0 0 8 11"><path d="M4 11 L1 5.5 A3.4 3.4 0 1 1 7 5.5Z" fill="#111"/><circle cx="4" cy="4" r="1.3" fill="#1a9fd6"/></svg></span>
          480 W Linden Ave
        </li>
      </ul>
    </div>
  </section>
</main>
</body>
</html>
```